Creat new BusinessCard for Brightpath Advisory!

Hello Creativ Designer. I need a new Businesscard for our brand new Company "Brightpath Coaching". We do Consulting for a better Life & Work Situation. to create Fulfillment, Sense, Motivation and healthy Work Places in Company's. So we try to create a better World and help the employee to like what they do!
So we would like to have 2 Sites on the card. On the Back we want to put this words: "The sole meaning of life, is to serve humanity" (it can be vertical oder horizontal). In the front there is the Logo (Black or White) and Adress+ and Slogan.

Slogan on the front: -Make your Business & Life to a better place-

Name: Lukas Fenwald
Titel: Founder - Visionary - Trainer
Adress: Based in Switzerland

Tel: +41 (0) 71 483 27 15
Email: hello@brightpath-coaching.ch
Homepage: www.brightpath-coaching.ch

Thanks for your inspired Ideas and your help to make the world to a better place! IT has to be ready to print and normal Size.

Target Market(s)

insurance, Bank, Telecom, industry, IT, Medical

Contact Information for Business Card

Breite: 85 mm x Höhe: 55 mm

Colors

Designer to choose colors to be used in the design.

Requirements
Nice to have
• Thanks for your Ideas so far!
• Maybe you can try/play with the colors: Purple Code #652C8F and Grey #979797 from the Zorvik Logo purple and grey (but only a soft combination, not to much)

```html
<!DOCTYPE html>
<html lang="en">
<head>
<meta charset="utf-8">
<title>Brightpath Coaching – Business Card</title>
<link href="https://fonts.googleapis.com/css2?family=Open+Sans:wght@400;600;700;800&display=swap" rel="stylesheet">
<style>
  :root {
    --stage: #dcdcdc;
    --card-dark: #1e1f21;
    --card-light: #fbfbfb;
    --ink: #141414;
    --ink-soft: #6f6f6f;
    --rule: #9a9a9a;
    --white: #ffffff;
  }
  * { box-sizing: border-box; margin: 0; padding: 0; }
  html, body { width: 1200px; height: 900px; overflow: hidden; }
  body {
    background: var(--stage);
    font-family: "Open Sans", Arial, sans-serif;
    display: flex;
    flex-direction: column;
    align-items: center;
    justify-content: center;
    gap: 40px;
  }
  .card {
    width: 600px;
    height: 388px;
    position: relative;
    box-shadow: 0 6px 18px rgba(0,0,0,.18);
  }

  /* Back side */
  .card--back {
    background: var(--card-dark);
    color: var(--white);
  }
  .back-mark {
    position: absolute;
    left: 50%;
    top: 62px;
    transform: translateX(-50%);
    display: flex;
    align-items: center;
    gap: 18px;
  }
  .back-mark__dot {
    width: 150px; height: 150px;
    border-radius: 50%;
    background: var(--white);
  }
  .back-mark__name {
    font-weight: 800;
    font-size: 26px;
    letter-spacing: .5px;
    text-transform: uppercase;
    line-height: 1.1;
    color: var(--white);
  }
  .back-quote {
    position: absolute;
    left: 0; right: 0;
    bottom: 56px;
    text-align: center;
    font-weight: 700;
    font-size: 17px;
  }

  /* Front side */
  .card--front {
    background: var(--card-light);
    color: var(--ink);
  }
  .person {
    position: absolute;
    top: 40px;
    right: 44px;
    text-align: right;
  }
  .person__name {
    font-weight: 800;
    font-size: 21px;
    text-transform: uppercase;
    letter-spacing: .3px;
  }
  .person__title {
    font-weight: 400;
    font-size: 15px;
    color: var(--ink-soft);
    text-transform: uppercase;
    letter-spacing: .5px;
    margin-top: 2px;
  }
  .person__slogan {
    font-weight: 600;
    font-size: 13px;
    color: var(--ink);
    margin-top: 12px;
  }
  .brand {
    position: absolute;
    left: 48px;
    top: 160px;
    display: flex;
    align-items: center;
    gap: 14px;
  }
  .brand__dot {
    width: 74px; height: 74px;
    border-radius: 50%;
    background: var(--ink);
  }
  .brand__name {
    font-weight: 800;
    font-size: 24px;
    text-transform: uppercase;
    line-height: 1.05;
    color: var(--ink);
    border-bottom: 1px solid var(--rule);
    padding-bottom: 4px;
  }
  .contacts {
    position: absolute;
    left: 48px;
    bottom: 30px;
    list-style: none;
    font-size: 15px;
    color: var(--ink-soft);
  }
  .contacts li {
    display: flex;
    align-items: center;
    gap: 10px;
    line-height: 22px;
  }
  .contacts svg { width: 14px; height: 14px; fill: var(--ink); flex: none; }
</style>
</head>
<body>

<section class="card card--back" aria-label="Card back">
  <div class="back-mark">
    <div class="back-mark__dot"></div>
    <div class="back-mark__name">Brightpath<br>Coaching</div>
  </div>
  <p class="back-quote">The sole meaning of life, is to serve humanity</p>
</section>

<section class="card card--front" aria-label="Card front">
  <div class="person">
    <p class="person__name">Lukas Fenwald</p>
    <p class="person__title">Founder - Visionary - Trainer</p>
    <p class="person__slogan">- Make your Business &amp; Life to a better place -</p>
  </div>

  <div class="brand">
    <div class="brand__dot"></div>
    <div class="brand__name">Brightpath<br>Coaching</div>
  </div>

  <ul class="contacts">
    <li>
      <svg viewBox="0 0 16 16" aria-hidden="true"><path d="M3.5 1 6 1.5 7 5 5.3 6.3a9 9 0 0 0 4.4 4.4L11 9l3.5 1 .5 2.5-2 2C6.5 14.5 1.5 9.5 1.5 3z"/></svg>
      +41 (0) 71 483 27 15
    </li>
    <li>
      <svg viewBox="0 0 16 16" aria-hidden="true"><path d="M1 3h14v10H1z" fill="none" stroke="#141414" stroke-width="1.6"/><path d="M1 3l7 6 7-6" fill="none" stroke="#141414" stroke-width="1.6"/></svg>
      hello@brightpath-coaching.ch
    </li>
    <li>
      <svg viewBox="0 0 16 16" aria-hidden="true"><circle cx="8" cy="8" r="7"/><circle cx="8" cy="8" r="3" fill="#fbfbfb"/></svg>
      www.brightpath-coaching.ch
    </li>
    <li>
      <svg viewBox="0 0 16 16" aria-hidden="true"><path d="M8 1a5 5 0 0 0-5 5c0 3.8 5 9 5 9s5-5.2 5-9a5 5 0 0 0-5-5z"/><circle cx="8" cy="6" r="2" fill="#fbfbfb"/></svg>
      Based in Switzerland
    </li>
  </ul>
</section>

</body>
</html>
```